Online-Marketing Material für medizinischen Online Ratgeber
Zielgruppe
Die Welt der Thoraxmedizin kann komplex und verwirrend sein. Orvena Linde steht für kompetente Beratung und verlässliche Informationen rund um das Thema Thoraxerkrankungen – entstanden aus dem Wunsch, umfassende Informationen zur Verfügung zu stellen Ob Lungenkrebs, Asthma, COPD oder Schlafapnoe – wir bringen Klarheit in alle Aspekte der ThoraxmedizinThorax Schweiz ist nicht nur eine Informationsplattform, sondern auch eine Gemeinschaft, in der jeder willkommen und eingeladen ist, Fragen zu stellen, sein Wissen zu erweitern und zu teilen.
Aufgabenstellung
Orvena Linde ist ein online Ratgeber im Bereich der thorax Erkrankungen. wir wollen mit dem facebook Auftritt die Webseite ergänzen.Wir benötigen für facebook ein Profilbanner (1200x630), ein Profilbild 800x800) sowie einen Entwurf für ein posting(800x800). Die Farben die verwendet werden solltenund das Logo von orvena linde habe ich im Anhang beigefügt.Ich bedanke mich schon jetzt für Ihre Mühe und freue mich auf Ihre Entwürfe.

```html
<!DOCTYPE html>
<html lang="de">
<head>
<meta charset="utf-8">
<title>Orvena Linde – Facebook Set</title>
<link href="https://fonts.googleapis.com/css2?family=Bebas+Neue&family=Roboto+Condensed:wght@600;700&family=Montserrat:wght@700&display=swap" rel="stylesheet">
<style>
  :root {
    --page: #ffffff;
    --navy-deep: #0b1430;
    --navy: #13305e;
    --brand-blue: #0a94d4;
    --accent-blue: #1a8fd6;
    --logo-blue: #124a9c;
    --glow: #2a7fd9;
    --white: #ffffff;
  }
  * { margin: 0; padding: 0; box-sizing: border-box; }
  html, body { width: 1200px; height: 848px; overflow: hidden; background: var(--page); }
  .canvas { position: relative; width: 1200px; height: 848px; }

  .cover-banner {
    position: absolute; left: 238px; top: 72px; width: 680px; height: 357px;
    overflow: hidden;
    background: radial-gradient(ellipse at 70% 50%, #1d4f9c 0%, #102a5e 35%, var(--navy-deep) 75%);
  }
  .cover-banner .lung-artwork {
    position: absolute; left: 340px; top: 0; width: 340px; height: 357px;
    background: radial-gradient(ellipse at 45% 60%, rgba(90,170,255,.55) 0%, rgba(42,127,217,.35) 40%, rgba(16,42,94,0) 75%);
  }
  .cover-headline {
    position: absolute; font-family: 'Bebas Neue', sans-serif; color: var(--white);
    font-size: 52px; line-height: 1; letter-spacing: .5px; white-space: nowrap;
  }
  .cover-headline .highlight { color: var(--accent-blue); }
  .cover-headline.line-one { left: 84px; top: 127px; }
  .cover-headline.line-two { left: 166px; top: 182px; }

  .profile-badge {
    position: absolute; left: 296px; top: 358px; width: 168px; height: 168px;
    border-radius: 50%; background: var(--white); border: 3px solid var(--brand-blue);
    display: flex; flex-direction: column; align-items: center; justify-content: center;
    font-family: 'Montserrat', sans-serif; font-weight: 700; color: var(--logo-blue);
    font-size: 22px; line-height: 1.05; text-align: center;
  }

  .fact-post {
    position: absolute; left: 533px; top: 463px; width: 331px; height: 331px;
    background: var(--brand-blue); text-align: center;
    font-family: 'Roboto Condensed', sans-serif; color: var(--white);
  }
  .fact-label {
    position: absolute; left: 85px; top: 62px; width: 154px; height: 28px;
    background: var(--navy); font-weight: 600; font-size: 19px; line-height: 28px;
  }
  .fact-statement {
    position: absolute; left: 0; right: 0; top: 99px;
    font-weight: 700; font-size: 41px; line-height: 42px;
  }
  .fact-statement .figure { color: var(--navy); }
  .fact-brand {
    position: absolute; left: 0; right: 0; bottom: 16px;
    font-family: 'Montserrat', sans-serif; font-weight: 700; font-size: 16px; letter-spacing: .3px;
  }
</style>
</head>
<body>
<main class="canvas">
  <section class="cover-banner">
    <div class="lung-artwork" role="img" aria-label="Leuchtend blaue digitale Darstellung einer Lunge mit Netzwerkpunkten"></div>
    <h1 class="cover-headline line-one">Ihr <span class="highlight">Ratgeber</span> für</h1>
    <p class="cover-headline line-two">Thoraxmedizin</p>
  </section>

  <div class="profile-badge">
    <span>ORVENA</span>
    <span>LINDE</span>
  </div>

  <section class="fact-post">
    <div class="fact-label">Schon gewußt?</div>
    <p class="fact-statement">Lorem ipsum<br>est durum <span class="figure">80%</span><br>fertet dolu.</p>
    <div class="fact-brand">ORVENA LINDE</div>
  </section>
</main>
</body>
</html>
```